Meadowlark Dental Letterhead

Please design full color letterhead for meadowlark dental. Letterhead should match the motif of the business card. Print and logo should be confined to a one inch margin on top and bottom. The following info should be included:
Meadowlrk Dental with the tooth logo
Felix R. Dorran, DDS
Bright Modern Smiles, Friendly Local Touch
Phone #: 555.271.4086
Address: 24318-C N Larchmont, Alder Falls, KS

```html
<!DOCTYPE html>
<html lang="en">
<head>
<meta charset="utf-8">
<title>Meadowlark Dental Letterhead</title>
<link rel="stylesheet" href="https://fonts.googleapis.com/css2?family=Open+Sans:wght@400;600;700&family=Questrial&display=swap">
<style>
  :root {
    --paper: #ffffff;
    --ink: #4a4a4a;
    --ink-dark: #3c3f44;
    --muted: #7a7a7a;
    --blue: #2f6db5;
    --green: #4fd13a;
    --magenta: #d4197e;
    --orange: #f0522b;
    --steel: #3f73b8;
  }
  * { margin: 0; padding: 0; box-sizing: border-box; }
  html, body { width: 942px; height: 1200px; overflow: hidden; background: var(--paper); }
  .letterhead {
    position: relative;
    width: 942px;
    height: 1200px;
    background: var(--paper);
    font-family: "Open Sans", Arial, sans-serif;
    color: var(--ink);
  }
  .brand {
    position: absolute;
    left: 81px;
    top: 74px;
    display: flex;
    align-items: center;
    gap: 14px;
  }
  .brand-mark {
    width: 58px;
    height: 58px;
    background: var(--steel);
  }
  .brand-name {
    font-family: "Questrial", Arial, sans-serif;
    font-size: 33px;
    line-height: 1.05;
    letter-spacing: 1px;
    color: var(--ink-dark);
    text-transform: uppercase;
  }
  .contact {
    position: absolute;
    left: 584px;
    top: 72px;
    display: flex;
    font-size: 9.5px;
    line-height: 20px;
    text-transform: uppercase;
    color: var(--ink-dark);
  }
  .contact-doctor { width: 146px; }
  .contact-doctor .doctor-name { color: var(--blue); font-weight: 700; }
  .contact-divider { width: 2px; height: 50px; background: var(--green); margin-right: 12px; margin-top: 4px; }
  .contact-line { display: flex; align-items: center; gap: 6px; }
  .contact-line svg { width: 10px; height: 10px; fill: var(--blue); }
  .contact-line.indent { padding-left: 16px; }
  .meta {
    position: absolute;
    left: 125px;
    top: 258px;
    font-family: "Questrial", Arial, sans-serif;
    font-size: 11px;
    line-height: 16px;
    color: var(--ink-dark);
  }
  .meta strong { font-weight: 700; font-family: "Open Sans", Arial, sans-serif; font-size: 10.5px; }
  .letter {
    position: absolute;
    left: 125px;
    top: 303px;
    width: 735px;
  }
  .letter-body {
    font-size: 11.2px;
    line-height: 24.5px;
    color: var(--ink);
  }
  .letter-body p { margin-bottom: 24.5px; }
  .letter-body .salutation { margin-bottom: 0; }
  .letter-body p:last-child { margin-bottom: 0; }
  .signatory {
    margin-top: 20px;
    font-family: "Questrial", Arial, sans-serif;
  }
  .signatory-name { font-size: 22px; line-height: 24px; color: var(--ink-dark); letter-spacing: 0.5px; }
  .signatory-name b { font-family: "Open Sans", Arial, sans-serif; font-weight: 600; }
  .signatory-role { font-size: 11.5px; color: var(--muted); }
  .signature {
    margin-top: 26px;
    width: 250px;
    height: 115px;
    background: linear-gradient(135deg, #f4f4f4, #e6e6e6);
  }
  .footer-band {
    position: absolute;
    left: 0;
    top: 1172px;
    width: 942px;
    height: 14px;
    display: flex;
    align-items: center;
  }
  .band { height: 14px; }
  .band-magenta { width: 51px; background: var(--magenta); }
  .band-orange { width: 58px; background: var(--orange); }
  .band-blue { width: 62px; background: var(--steel); }
  .band-green-long { width: 468px; background: var(--green); }
  .band-green-end { flex: 1; background: var(--green); }
  .tagline {
    width: 227px;
    text-align: center;
    font-size: 10px;
    font-weight: 700;
    letter-spacing: 1.5px;
    color: var(--blue);
    text-transform: uppercase;
  }
</style>
</head>
<body>
<main class="letterhead">
  <header>
    <div class="brand">
      <div class="brand-mark"></div>
      <div class="brand-name">Meadowlark<br>Dental</div>
    </div>
    <div class="contact">
      <div class="contact-doctor">
        <div class="doctor-name">Felix R. Dorran, DDS</div>
        <div>Bright Modern Smiles</div>
        <div>Friendly Local Touch</div>
      </div>
      <div class="contact-divider"></div>
      <div class="contact-details">
        <div class="contact-line">
          <svg viewBox="0 0 24 24" aria-hidden="true"><path d="M6.6 10.8a15.1 15.1 0 0 0 6.6 6.6l2.2-2.2a1 1 0 0 1 1-.25 11.4 11.4 0 0 0 3.6.57 1 1 0 0 1 1 1V20a1 1 0 0 1-1 1A17 17 0 0 1 3 4a1 1 0 0 1 1-1h3.5a1 1 0 0 1 1 1c0 1.25.2 2.45.57 3.57a1 1 0 0 1-.25 1z"/></svg>
          555.271.4086
        </div>
        <div class="contact-line">
          <svg viewBox="0 0 24 24" aria-hidden="true"><path d="M12 2a7 7 0 0 0-7 7c0 5.25 7 13 7 13s7-7.75 7-13a7 7 0 0 0-7-7zm0 9.5A2.5 2.5 0 1 1 12 6.5a2.5 2.5 0 0 1 0 5z"/></svg>
          24318-C N Larchmont
        </div>
        <div class="contact-line indent">Alder Falls, KS 66020</div>
      </div>
    </div>
  </header>

  <div class="meta">
    <div><strong>Date :</strong> Mon , 25 / 3 / 2013</div>
    <div><strong>Recipient :</strong> Mr. Owen Tate Sanderson</div>
  </div>

  <section class="letter">
    <article class="letter-body">
      <p class="salutation">Dear Mr. Owen Tate</p>
      <p>Lorem ipsum dolor sit amet, consectetur adipiscing elit. Praesent vulputate, neque ac accumsan suscipit, justo turpis volutpat nisl, tempus fermentum eros tortor et elit. Vivamus porttitor faucibus gravida. Quisque pharetra gravida luctus. Donec eget turpis libero. Ut ac dolor urna, quis tempor nunc. Donec vitae mauris purus, euismod eleifend nulla. Lorem ipsum dolor sit amet, consectetur adipiscing elit. Donec ut purus tellus. Aenean quis dignissim lacus. Vestibulum suscipit vehicula cursus. Suspendisse potenti. Ut in sem nisi. Sed et massa leo.</p>
      <p>Fusce varius libero vel risus condimentum suscipit. Nullam tristique ultrices massa a volutpat. Donec sed dictum metus. Curabitur fringilla nibh eu ligula pharetra a interdum quam aliquam. Maecenas aliquam elit eu orci rutrum molestie. Proin nisl justo, varius a volutpat nec, ultricies sed sem. Nam sit amet imperdiet sem. Phasellus vitae mauris odio. Etiam in purus dui. Etiam ultricies, ante vel iaculis sodales, arcu leo adipiscing leo, sit amet mollis dui nisi non quam.</p>
      <p>Suspendisse sagittis laoreet dolor, vitae rhoncus arcu volutpat quis. Vestibulum at placerat dolor. Vivamus eu lacus ut enim molestie consectetur. Quisque ac lorem vel orci sagittis sollicitudin. Nunc ut quam sem, quis volutpat libero. Cum sociis natoque penatibus et magnis dis parturient montes, nascetur ridiculus mus. Vestibulum ante ipsum primis in faucibus orci luctus et ultrices posuere cubilia Curae; Donec tempor velit in velit feugiat sit amet vulputate nisl posuere..</p>
    </article>

    <div class="signatory">
      <div class="signatory-name"><b>OWEN</b> TATE</div>
      <div class="signatory-role">General director</div>
    </div>
    <div class="signature" role="img" aria-label="Handwritten signature of the general director"></div>
  </section>

  <footer class="footer-band">
    <div class="band band-magenta"></div>
    <div class="band band-orange"></div>
    <div class="band band-blue"></div>
    <div class="band band-green-long"></div>
    <div class="tagline">For all your dental needs</div>
    <div class="band band-green-end"></div>
  </footer>
</main>
</body>
</html>
```